Young Entrepreneur needs the sexiest, slickest, hottest ANDROID ALARM APP DESIGN.

Now that I have your attention...

The name of the Application is PlumDrift, using 'Stickers' this application is meant to get you to do what you need to do AND TO DO IT NOW, with a UI so simple my grandma can use it.

Using the provided sketches as a REFERENCE point, THREE (3) SCREENS will be needed, including a couple of design accents, which when the project is completed will be sent directly to a programming team.

Industry/Entity Type

Android

Requirements
Must have
• Creativity in simplicity. but please, go wild, do your 'thang'... Just keep it simple and clean.

```html
<!DOCTYPE html>
<html lang="en">
<head>
<meta charset="utf-8">
<title>PlumDrift – Alarm Edit</title>
<link rel="stylesheet" href="https://fonts.googleapis.com/css2?family=Open+Sans:wght@300;400;700&display=swap">
<style>
  :root {
    --stage: #eef2f6;
    --sky-top: #7fcfea;
    --sky-mid: #5cc0e6;
    --sky-deep: #35b0e1;
    --text-light: #ffffff;
    --text-faint: rgba(255,255,255,0.55);
    --dial-ring: #e3f3fa;
    --dial-face: #ffffff;
    --time-blue: #3aa9de;
    --label-grey: #9a9a9a;
  }
  * { margin: 0; padding: 0; box-sizing: border-box; }
  html, body {
    width: 1200px; height: 987px; overflow: hidden;
    background: var(--stage);
    font-family: "Open Sans", sans-serif;
  }
  .app-screen {
    position: absolute;
    left: 347px; top: 40px;
    width: 506px; height: 907px;
    background:
      radial-gradient(ellipse 70% 45% at 50% 38%, rgba(255,255,255,0.22), rgba(255,255,255,0) 70%),
      linear-gradient(160deg, var(--sky-top) 0%, var(--sky-mid) 45%, var(--sky-deep) 100%);
    overflow: hidden;
  }
  .day-row {
    position: absolute; top: 46px; left: 0; right: 0;
    display: flex; justify-content: space-around;
    padding: 0 22px;
    list-style: none;
    font-weight: 300; font-size: 19px; color: var(--text-light);
  }
  .day-row .is-off { color: var(--text-faint); }
  .alarm-dial {
    position: absolute; left: 93px; top: 130px;
    width: 320px; height: 320px;
  }
  .alarm-dial svg { position: absolute; inset: 0; }
  .alarm-readout {
    position: absolute; inset: 0;
    display: flex; flex-direction: column; align-items: center; justify-content: center;
  }
  .alarm-time {
    position: relative;
    font-weight: 700; font-size: 96px; line-height: 1; letter-spacing: -2px;
    color: var(--time-blue);
  }
  .alarm-meridiem {
    position: absolute; right: 2px; top: -20px;
    font-weight: 400; font-size: 20px; letter-spacing: 0; color: var(--label-grey);
  }
  .alarm-label {
    font-weight: 300; font-size: 40px; color: var(--label-grey);
    margin-top: 4px; padding-left: 60px;
  }
  .action-menu {
    position: absolute; left: 250px; top: 520px;
    list-style: none;
    font-weight: 300; font-size: 22px; color: var(--text-light);
    line-height: 40px;
  }
  .action-menu li:nth-child(2) { padding-left: 14px; }
  .action-menu li:nth-child(3) { padding-left: 22px; }
  .action-menu li:nth-child(4) { padding-left: 38px; }
  .action-menu li:nth-child(5) { padding-left: 34px; }
  .action-menu li:nth-child(6) { padding-left: 58px; }
  .brand-mark {
    position: absolute; left: 0; right: 0; top: 800px;
    display: flex; justify-content: center; align-items: center; gap: 8px;
    font-weight: 700; font-size: 22px; color: var(--text-light);
  }
  .brand-mark .dot {
    width: 10px; height: 10px; border-radius: 50%; background: var(--text-light);
  }
</style>
</head>
<body>
  <main class="app-screen">
    <ul class="day-row">
      <li>Mon</li><li>Tue</li><li>Wed</li><li>Thu</li><li>Fri</li>
      <li class="is-off">Sat</li><li class="is-off">Sun</li>
    </ul>

    <section class="alarm-dial">
      <svg viewBox="-160 -160 320 320" width="320" height="320" aria-hidden="true">
        <polygon fill="var(--dial-ring)" points="144.9,38.8 106.1,106.1 38.8,144.9 -38.8,144.9 -106.1,106.1 -144.9,38.8 -144.9,-38.8 -106.1,-106.1 -38.8,-144.9 38.8,-144.9 106.1,-106.1 144.9,-38.8"/>
        <polygon fill="var(--dial-face)" points="127.5,34.2 93.3,93.3 34.2,127.5 -34.2,127.5 -93.3,93.3 -127.5,34.2 -127.5,-34.2 -93.3,-93.3 -34.2,-127.5 34.2,-127.5 93.3,-93.3 127.5,-34.2"/>
      </svg>
      <div class="alarm-readout">
        <div class="alarm-time">6:40<span class="alarm-meridiem">am</span></div>
        <div class="alarm-label">Shower</div>
      </div>
    </section>

    <ul class="action-menu">
      <li>On/Off</li>
      <li>Delete</li>
      <li>Sounds</li>
      <li>Color</li>
      <li>Set Sticky</li>
      <li>Save</li>
    </ul>

    <div class="brand-mark"><span class="dot"></span>PlumDrift</div>
  </main>
</body>
</html>
```